plovu business card design

plovu is an incubator within RTM Media focused on unlocking the potential in underserved niche micro-verticals on the web. our mission is to rapidly develop and foster emerging micro-verticals bc they are ripe for growth - building interesting and trusted content experiences with unqiue, useful and cutting-edge delivery methods.please do all copy (except for RTM Media, which must look as typed here and in logo) in all lowercase. Also please use spaces between phone # extensions not dashes or periods. I have attached all variations of the logo.
Industry/Entity Type
Business
Contact Information for Business Card
daria feltow, ceo www.plovu.io 218 holbrook lane 3rd floor oakland ca 94731 415 602 0002m 510 985 7966d daria.feltow@plovu.io
Look and feel
Each slider illustrates characteristics of the customer's brand and the style your logo design should communicate.

```html
<!DOCTYPE html>
<html lang="en">
<head>
<meta charset="utf-8">
<title>plovu business card</title>
<link rel="stylesheet" href="https://fonts.googleapis.com/css2?family=Lato:wght@400&family=Montserrat:wght@400&family=Open+Sans:wght@600;700&display=swap">
<style>
  :root {
    --backdrop: #141414;
    --paper: #f3f3f3;
    --teal: #007f7b;
    --teal-light: #0a8e89;
    --teal-dark: #00706c;
    --ink: #1f1f1f;
    --white: #ffffff;
  }
  * { margin: 0; padding: 0; box-sizing: border-box; }
  html, body {
    width: 1200px; height: 900px; overflow: hidden;
    background: var(--backdrop);
  }
  .stage { position: relative; width: 1200px; height: 900px; }
  .card {
    position: absolute; top: 184px; width: 302px; height: 490px;
    border-radius: 13px; overflow: hidden;
  }
  .card--front { left: 299px; background: var(--paper); color: var(--ink); }
  .card--back { left: 646px; background: var(--teal); color: var(--white); }

  .wordmark {
    position: absolute; display: flex; align-items: center; gap: 8px;
    font-family: "Open Sans", sans-serif; font-weight: 700; letter-spacing: -1px;
    line-height: 1;
  }
  .wordmark__dot { display: block; border-radius: 50%; }
  .tagline {
    position: absolute; font-family: "Montserrat", sans-serif; font-weight: 400;
    white-space: nowrap;
  }

  .card--front .wordmark { left: 36px; top: 48px; font-size: 60px; color: var(--ink); }
  .card--front .wordmark__dot { width: 16px; height: 16px; background: var(--teal); margin-top: 20px; }
  .card--front .tagline { left: 38px; top: 128px; font-size: 12.5px; color: var(--ink); }

  .person { position: absolute; left: 36px; top: 250px; }
  .person__name {
    font-family: "Open Sans", sans-serif; font-weight: 600; font-size: 17px;
    color: var(--teal); line-height: 1.2;
  }
  .person__role { font-family: "Lato", sans-serif; font-size: 16px; line-height: 1.2; }

  .contact {
    position: absolute; left: 36px; top: 312px; list-style: none;
    font-family: "Lato", sans-serif; font-size: 14px; line-height: 20.3px;
  }
  .contact__label { color: var(--teal); }
  .address {
    position: absolute; left: 36px; top: 411px; font-style: normal;
    font-family: "Lato", sans-serif; font-size: 14px; line-height: 18px;
  }

  .card__texture {
    position: absolute; inset: 0;
    background: radial-gradient(ellipse at 45% 50%, var(--teal-light) 0%, var(--teal) 45%, var(--teal-dark) 100%);
  }
  .card--back .wordmark {
    left: 0; right: 0; top: 210px; justify-content: center;
    font-size: 54px; color: var(--white);
  }
  .card--back .tagline {
    left: 0; right: 0; top: 266px; text-align: center; font-size: 11px; color: var(--white);
  }
</style>
</head>
<body>
<main class="stage">
  <section class="card card--front" aria-label="card front">
    <div class="wordmark">plovu<span class="wordmark__dot"></span></div>
    <p class="tagline">an RTM Media incubator</p>
    <div class="person">
      <p class="person__name">daria feltow</p>
      <p class="person__role">ceo</p>
    </div>
    <ul class="contact">
      <li><span class="contact__label">m:</span> 415 738 4196</li>
      <li><span class="contact__label">d:</span> 510 247 3859</li>
      <li><span class="contact__label">e:</span> daria.feltow@plovu.io</li>
      <li><span class="contact__label">w:</span> www.plovu.io</li>
    </ul>
    <address class="address">218 holbrook lane 3rd<br>floor oakland ca 94731</address>
  </section>

  <section class="card card--back" aria-label="card back">
    <div class="card__texture" role="img" aria-label="embossed ink splash texture across the card"></div>
    <div class="wordmark">plovu</div>
    <p class="tagline">an RTM Media incubator</p>
  </section>
</main>
</body>
</html>
```